One of Australia's fastest growing energy maintenance contractors needs a new website

www.brightpane.com.au
Our business has evolved over the past years and now our website is no longer relevant.
We clean solar panels and we vacuum roof gutters.
We clean solar panels on the roofs of residential houses right up to billion dollar solar farms with in excess of 1 million panels. We offer thermal image testing and bird proofing for our residential and commercial clients and thermal drone imaging services for our solar farm clients.
We vacuum clean roof gutters (using a LoftSuk) on the residential house next door right up to enormous private and public schools, colleges, shopping centres, strat complexes and commercial buildings.
When first built our business had more of a domestic residential skew and the website reflected that. While that is still part of our core business we are now bidding on and have secured large government, commercial and infrastructure contracts and our new website needs to reflect our growth and our new business. We need a new site that it optimised for both desktop ad phone viewing as our latest figures showed that 73% of people visiting our site are on mobile phones. We have an extensive amount of data on Vesti Metrics available as well as Promos. Both that would also need integrating with the site along with a few other plugins such as Qarlo Chat Desk, Pallio etc along with SEO key words etc. We are also the winner and finalists over multiple years of the small business of the year awards and we like to proudly and prominently display those on our site.
We are looking for a new site with a modern professional feel / theme
There is a definitive break in our business between the solar Panel cleaning clients and the gutter cleaning clients so we would like a home page that begins with a simple choice:
Solar Panel Cleaning – Gutter Cleaning
With a professional full screen background image (we have hundreds to choose from) and along the bottom a small area with rights reserved etc, phone number etc (at some point in the future we will split these into two businesses but for now it’s what we have).
After that selection is made we would like a repeat of that same scenario but the selection is:
If it’s Solar Panel Cleaning
(new background image)
Government – Infrastructure – Commercial – Residential
If it’s Gutter Cleaning
(new background image)
Government – Strata – Commercial – Residential
After making those choices then onto the relevant pages with background images relevant to each sector and a them that suits (on the residential we would like to keep the link to our vesti ratings) - We will provide copy / text for each relevant page.
Other than that, a menu inclusive of the above and:
Resellers Portal – we will provide a link to this from Qarlo CRM)
Customer portal (we will supply a link to this from our booking system)
We also need a page for our Solar Resellers / Partners page but we will give them a link to this, it won’t be listed on the site.
Request a quote page (Again we will provide information from Qarlo as this will be linked to the CRM)
Standard contact us page inclusive of phone numbers, address and fields supplied from CRM
Sydney – 02 7391 5083
Southern Highlands – 02 4860 3178
Goulburn – 02 4860 3178
Canberra – 02 6172 8354
Wollongong – 02 4239 6017
sales@brightpane.com.au
Head Office - Ferndale Rise NSW 2590
ABN: 48906237115
Responsive Design: Optimized for desktop and mobile (73% mobile visitors).
Fast Loading Speed: Optimized for performance.
Smooth Transition Animations: For service and category selection.
Sticky Contact Bar: Always accessible at the bottom of mobile screens for quick calls.
SEO Optimization: Focused on government tenders, large-scale commercial contracts, and infrastructure projects.
Integrations
Vesti Metrics & Vesti Promos.
Qarlo Chat Desk.
Pallio Beacon.
SEO tools and keyword optimization.
Many many more images available if needed

```html
<!DOCTYPE html>
<html lang="en">
<head>
<meta charset="utf-8">
<title>BrightPane – Premier Solar Panel Cleaning</title>
<link href="https://fonts.googleapis.com/css2?family=Figtree:ital,wght@0,300;0,400;0,500;0,600;0,700;1,500&display=swap" rel="stylesheet">
<style>
:root{
  --blue:#0661ad;
  --blue-dark:#054f8e;
  --cyan:#1fade4;
  --ink:#111418;
  --muted:#5b6068;
  --line:#dcdfe3;
  --soft:#f4f4f4;
  --gold:#e8a317;
  --white:#ffffff;
  --footer:#000000;
}
*{box-sizing:border-box;margin:0;padding:0}
html,body{width:1200px;height:3610px;overflow:hidden}
body{position:relative;font-family:"Figtree",sans-serif;color:var(--ink);background:var(--white)}
.abs{position:absolute}
.btn{position:absolute;display:flex;align-items:center;justify-content:center;gap:8px;height:36px;border-radius:18px;font-size:10.5px;font-weight:600;border:1.3px solid var(--blue);color:var(--blue);background:transparent}
.btn.light{border-color:var(--white);color:var(--white)}
.btn svg{width:14px;height:8px}

/* header */
.site-header{position:absolute;left:0;top:0;width:1200px;height:62px;background:var(--white);z-index:3}
.logo-tab{position:absolute;left:106px;top:0;width:140px;height:128px;z-index:4}
.brand{position:absolute;left:122px;top:48px;width:110px;text-align:center;font-size:16px;font-weight:600;color:var(--blue);z-index:5}
.brand-mark{position:absolute;left:167px;top:20px;width:20px;height:20px;background:var(--blue);z-index:5}
.nav{position:absolute;top:24px;font-size:10.5px;font-weight:500;color:var(--ink);z-index:5}
.nav.active{color:var(--blue);font-style:italic}
.nav.active::after{content:"";position:absolute;left:0;right:0;top:26px;height:2px;background:var(--blue)}

/* hero */
.hero{position:absolute;left:0;top:62px;width:1200px;height:532px;background:linear-gradient(100deg,#3c4a58 0%,#5d6b72 35%,#7a7c68 60%,#6d6a55 100%)}
.hero::after{content:"";position:absolute;inset:0;background:rgba(10,20,35,.35)}
.hero h1{position:absolute;left:0;width:1200px;top:182px;text-align:center;font-size:53px;font-weight:400;color:var(--white);z-index:2;letter-spacing:.2px}
.hero p{position:absolute;left:0;width:1200px;top:266px;text-align:center;font-size:23px;line-height:34px;font-weight:300;color:var(--white);z-index:2}

/* sectors */
.sectors{position:absolute;left:0;top:594px;width:1200px;height:525px;background:var(--blue)}
.section-title-light{position:absolute;left:0;width:1200px;text-align:center;color:var(--white);font-size:24px;font-weight:400}
.sector-img{position:absolute;top:139px;width:181px;height:219px}
.sector-label{position:absolute;top:368px;width:181px;text-align:center;color:var(--white);font-size:12px;font-weight:600}

/* reviews */
.h2{position:absolute;left:0;width:1200px;text-align:center;font-size:38px;font-weight:400;color:var(--ink)}
.rating{position:absolute;left:0;width:1200px;top:1258px;text-align:center;font-size:9px;color:var(--muted)}
.rating b{color:var(--blue);font-weight:600}
.rating .stars{color:var(--gold);font-size:11px;letter-spacing:1px}
.card{position:absolute;top:1302px;width:251px;height:249px;background:var(--white);box-shadow:0 2px 8px rgba(0,0,0,.12);text-align:center}
.card .quote{position:absolute;left:107px;top:20px;width:37px;height:37px;border-radius:50%;background:#f1f3f6;color:var(--blue);font-size:22px;font-weight:700;line-height:44px}
.card .stars{position:absolute;left:0;right:0;top:64px;color:var(--gold);font-size:15px;letter-spacing:2px}
.card .text{position:absolute;left:18px;right:18px;top:95px;font-size:9px;line-height:15px;color:#333}
.card .name{position:absolute;left:0;right:0;top:201px;font-size:11px;font-weight:600}
.card .verified{position:absolute;left:0;right:0;top:220px;font-size:8px;color:#8a8f96}
.card .verified i{display:inline-block;width:8px;height:8px;border-radius:50%;background:var(--blue);margin-right:4px;vertical-align:-1px}
.arrow-btn{position:absolute;top:1412px;width:25px;height:25px;border-radius:50%;border:1.2px solid var(--blue)}

/* why */
.why{position:absolute;left:0;top:1695px;width:1200px;height:428px;background:var(--soft)}
.feature{position:absolute;top:160px;width:190px;text-align:center}
.feature svg{width:42px;height:42px}
.feature h3{font-size:13px;font-weight:500;margin-top:8px}
.feature p{font-size:9px;line-height:15px;color:var(--muted);margin-top:6px}
.divider{position:absolute;top:158px;width:1px;height:124px;background:var(--line)}

/* explore */
.acc-row{position:absolute;left:262px;width:675px;border-bottom:1px solid var(--line);font-size:20px;font-weight:400;padding-left:25px;display:flex;align-items:center}
.acc-row .chev{position:absolute;right:25px;top:50%;width:18px;height:8px;margin-top:-4px}
.acc-open{position:absolute;left:262px;top:2330px;width:675px;height:272px;background:var(--soft);border-bottom:1px solid var(--line)}
.acc-open h4{position:absolute;left:25px;top:13px;font-size:21px;font-weight:500;color:var(--blue)}
.acc-open p{position:absolute;left:25px;top:94px;width:300px;font-size:8.6px;line-height:15px;color:#333}

/* banner */
.banner{position:absolute;left:0;top:2918px;width:1200px;height:312px;background:var(--cyan);overflow:hidden}
.banner h2{position:absolute;left:107px;top:66px;font-size:38px;line-height:54px;font-weight:400;color:var(--white)}

/* footer */
.footer{position:absolute;left:0;top:3230px;width:1200px;height:380px;background:var(--footer);color:var(--white)}
.f-brand{position:absolute;left:200px;top:190px;font-size:33px;font-weight:500}
.f-mark{position:absolute;left:257px;top:95px;width:70px;height:70px;background:var(--blue)}
.f-head{position:absolute;top:78px;font-size:12px;font-weight:500;display:flex;align-items:center;gap:16px}
.f-head span{display:block;height:1px;background:#8a8a8a}
.f-list{position:absolute;list-style:none;font-size:9.5px}
.f-list li{height:25px;display:flex;align-items:center;gap:8px}
.f-list b{font-weight:600}
.f-list svg{width:9px;height:9px;flex:none}
.social{position:absolute;left:969px;width:30px;height:30px;border-radius:50%;background:#3a3a3a}
.legal{position:absolute;top:316px;font-size:9px}
</style>
</head>
<body>

<!-- Header -->
<header class="site-header">
  <span class="nav" style="left:540px">Home</span>
  <span class="nav active" style="left:604px">Solar Cleaning</span>
  <span class="nav" style="left:704px">Gutter Cleaning</span>
  <span class="nav" style="left:808px">Dustora</span>
  <span class="nav" style="left:878px">Contact us</span>
  <span class="btn" style="left:956px;top:13px;width:137px;font-size:10px">Request a Quote
    <svg viewBox="0 0 14 8"><path d="M0 4h12M9 1l3 3-3 3" fill="none" stroke="currentColor" stroke-width="1"/></svg></span>
</header>
<svg class="logo-tab" viewBox="0 0 140 128" aria-hidden="true"><polygon points="0,0 140,0 140,62 70,128 0,62" fill="#fff"/></svg>
<span class="brand-mark"></span>
<div class="brand">BrightPane</div>

<!-- Hero -->
<section class="hero" role="img" aria-label="Worker in a hard hat cleaning rooftop solar panels with a long pole brush">
  <h1>Premier Solar Panel Cleaning</h1>
  <p>We have a detailed knowledge of the cleaning &amp; testing<br>of Solar Panels</p>
  <span class="btn light" style="left:531px;top:364px;width:137px;z-index:2">Request a Quote
    <svg viewBox="0 0 14 8"><path d="M0 4h12M9 1l3 3-3 3" fill="none" stroke="currentColor" stroke-width="1"/></svg></span>
</section>

<!-- Service sectors -->
<section class="sectors">
  <h2 class="section-title-light" style="top:77px">Service sectors</h2>
  <div class="sector-img" style="left:200px;background:linear-gradient(180deg,#7fa9d6 0%,#c9d3dc 55%,#6f8f4f 100%)" role="img" aria-label="Domed government building"></div>
  <div class="sector-img" style="left:407px;background:linear-gradient(180deg,#2a3a5a 0%,#6b6a72 45%,#c9953a 100%)" role="img" aria-label="City infrastructure at dusk"></div>
  <div class="sector-img" style="left:613px;background:linear-gradient(180deg,#9fc1e4 0%,#5d7893 50%,#2c3e52 100%)" role="img" aria-label="Commercial glass towers"></div>
  <div class="sector-img" style="left:819px;background:linear-gradient(180deg,#c8d5e0 0%,#b7aa93 50%,#6f9150 100%)" role="img" aria-label="Two-storey residential house"></div>
  <div class="sector-label" style="left:200px">Government</div>
  <div class="sector-label" style="left:407px">Infrastructure</div>
  <div class="sector-label" style="left:613px">Commercial</div>
  <div class="sector-label" style="left:819px">Residential</div>
  <span class="btn light" style="left:531px;top:412px;width:137px">Request a Quote
    <svg viewBox="0 0 14 8"><path d="M0 4h12M9 1l3 3-3 3" fill="none" stroke="currentColor" stroke-width="1"/></svg></span>
</section>

<!-- Reviews -->
<h2 class="h2" style="top:1196px">We Love Happy Customers</h2>
<div class="rating"><b>Excellent:</b> &nbsp;<span class="stars">★★★★★</span> <b>4.9</b> based on <b>392</b> reviews</div>

<span class="arrow-btn" style="left:144px"><svg viewBox="0 0 25 25"><path d="M16 12.5H9M11.5 10l-2.5 2.5 2.5 2.5" fill="none" stroke="#0661ad" stroke-width="1"/></svg></span>
<span class="arrow-btn" style="left:1031px"><svg viewBox="0 0 25 25"><path d="M9 12.5h7M13.5 10l2.5 2.5-2.5 2.5" fill="none" stroke="#0661ad" stroke-width="1"/></svg></span>

<article class="card" style="left:200px">
  <span class="quote">“</span><div class="stars">★★★★★</div>
  <p class="text">Another excellent service from BrightPane. arrived on time and completed the job well. easy to deal with and great technician.<br>we will have them again.</p>
  <div class="name">Harlan Sweeting</div><div class="verified"><i></i>Verified Customer</div>
</article>
<article class="card" style="left:477px">
  <span class="quote">“</span><div class="stars">★★★★★</div>
  <p class="text">This is the third year the guys from brightpane have cleaned my gutters and i am very happy to recommend them. my job is not an easy one, double story with valleys and skylights in difficult places to access and the many before and after photos they attach to the...</p>
  <div class="name">Ross Hadley</div><div class="verified"><i></i>Verified Customer</div>
</article>
<article class="card" style="left:752px">
  <span class="quote">“</span><div class="stars">★★★★★</div>
  <p class="text">Amazing job cleaning out my gutters.<br>it was sunny and very hot. definitely a lot more dirt in the gutters than i expected and a bit of extra work but no complaints from the cleaner. great work. would recommend to friends and family.</p>
  <div class="name">Nate K</div><div class="verified"><i></i>Verified Customer</div>
</article>

<span class="btn" style="left:531px;top:1582px;width:137px">View all Review
  <svg viewBox="0 0 14 8"><path d="M0 4h12M9 1l3 3-3 3" fill="none" stroke="currentColor" stroke-width="1"/></svg></span>

<!-- Why clean -->
<section class="why">
  <h2 class="h2" style="top:76px">Why Clean Your Panels?</h2>
  <div class="feature" style="left:195px">
    <svg viewBox="0 0 42 42"><circle cx="13" cy="12" r="8" fill="none" stroke="#0661ad" stroke-width="1.5"/><circle cx="13" cy="12" r="3" fill="#0661ad"/><path d="M20 38V26M26 38V20M32 38V14M8 38h30" stroke="#555" stroke-width="1.5" fill="none"/></svg>
    <h3>Increased Efficiency</h3><p>Maintain and increase<br>the efficiency of your panels</p>
  </div>
  <div class="divider" style="left:394px"></div>
  <div class="feature" style="left:403px">
    <svg viewBox="0 0 42 42"><circle cx="21" cy="17" r="13" fill="none" stroke="#555" stroke-width="1.5"/><circle cx="21" cy="17" r="8" fill="none" stroke="#0661ad" stroke-width="1.5"/><path d="M21 12l1.6 3.3 3.6.5-2.6 2.5.6 3.6-3.2-1.7-3.2 1.7.6-3.6-2.6-2.5 3.6-.5z" fill="#0661ad"/><path d="M13 28l-3 10 5-2 3 4 3-8M29 28l3 10-5-2-3 4-3-8" fill="none" stroke="#555" stroke-width="1.3"/></svg>
    <h3>Maintain Warranty</h3><p>Maintain warranty obligations</p>
  </div>
  <div class="divider" style="left:600px"></div>
  <div class="feature" style="left:607px">
    <svg viewBox="0 0 42 42"><circle cx="21" cy="19" r="3" fill="#0661ad"/><path d="M21 16c-2-5 0-10 3-11 2 3 0 8-3 11zM23.5 20.5c5 1 8 5 7 8-4 0-7-4-7-8zM18.5 20.5c-5 1-8 5-7 8 4 0 7-4 7-8z" fill="none" stroke="#0661ad" stroke-width="1.4"/><path d="M21 22v16M15 38h12" stroke="#555" stroke-width="1.5"/></svg>
    <h3>Increase Power Output</h3><p>Increase energy output by<br>20% or more</p>
  </div>
  <div class="divider" style="left:806px"></div>
  <div class="feature" style="left:814px">
    <svg viewBox="0 0 42 42"><path d="M21 4l14 5v11c0 9-6 15-14 18C13 35 7 29 7 20V9z" fill="none" stroke="#555" stroke-width="1.5"/><circle cx="21" cy="20" r="6" fill="none" stroke="#0661ad" stroke-width="1.5"/><path d="M21 11v3M21 26v3M12 20h3M27 20h3M15 14l2 2M25 24l2 2M27 14l-2 2M15 26l2-2" stroke="#0661ad" stroke-width="1.3"/></svg>
    <h3>No Contact Covid Safe</h3><p>We use a contactless and covid<br>safe system</p>
  </div>
  <span class="btn" style="left:531px;top:316px;width:137px">Request a Quote
    <svg viewBox="0 0 14 8"><path d="M0 4h12M9 1l3 3-3 3" fill="none" stroke="currentColor" stroke-width="1"/></svg></span>
</section>

<!-- Explore -->
<h2 class="h2" style="top:2200px">Explore Solar Panel Cleaning</h2>

<div class="acc-row" style="top:2282px;height:48px;border-top:1px solid var(--line)">About panel soiling
  <svg class="chev" viewBox="0 0 18 8"><path d="M1 2l6 4 6-4" fill="none" stroke="#0661ad" stroke-width="2"/><circle cx="16" cy="3" r="1.2" fill="#0661ad"/></svg></div>

<div class="acc-open">
  <h4>Rain washes my panels</h4>
  <svg class="abs" style="right:25px;top:22px;width:18px;height:8px" viewBox="0 0 18 8"><path d="M1 6l6-4 6 4" fill="none" stroke="#0661ad" stroke-width="2"/><circle cx="16" cy="5" r="1.2" fill="#0661ad"/></svg>
  <p>Answer this; does rain wash your car? even in milder climactic conditions with more rainy weather, it is noticeable that dirt will remain on the panels. this is true even when modules are installed at a steep incline, which helps to flush off water and dirt. moreover, dust tends to accumulate over time, and will</p>
  <span class="btn" style="left:25px;top:193px;width:111px">Learn More
    <svg viewBox="0 0 14 8"><path d="M0 4h12M9 1l3 3-3 3" fill="none" stroke="currentColor" stroke-width="1"/></svg></span>
  <div class="abs" style="left:400px;top:65px;width:249px;height:188px;background:linear-gradient(160deg,#7fa0c4 0%,#3f5f86 45%,#c9a53a 70%,#2f4058 100%)" role="img" aria-label="Worker in yellow protective gear pressure-washing solar panels"></div>
</div>

<div class="acc-row" style="top:2602px;height:48px">Management plan
  <svg class="chev" viewBox="0 0 18 8"><path d="M1 2l6 4 6-4" fill="none" stroke="#0661ad" stroke-width="2"/><circle cx="16" cy="3" r="1.2" fill="#0661ad"/></svg></div>
<div class="acc-row" style="top:2650px;height:49px">Beyond dust
  <svg class="chev" viewBox="0 0 18 8"><path d="M1 2l6 4 6-4" fill="none" stroke="#0661ad" stroke-width="2"/><circle cx="16" cy="3" r="1.2" fill="#0661ad"/></svg></div>
<div class="acc-row" style="top:2699px;height:50px">Power loss
  <svg class="chev" viewBox="0 0 18 8"><path d="M1 2l6 4 6-4" fill="none" stroke="#0661ad" stroke-width="2"/><circle cx="16" cy="3" r="1.2" fill="#0661ad"/></svg></div>
<div class="acc-row" style="top:2749px;height:49px">Do they really need cleaning?
  <svg class="chev" viewBox="0 0 18 8"><path d="M1 2l6 4 6-4" fill="none" stroke="#0661ad" stroke-width="2"/><circle cx="16" cy="3" r="1.2" fill="#0661ad"/></svg></div>

<span class="btn" style="left:531px;top:2831px;width:137px">Request a Quote
  <svg viewBox="0 0 14 8"><path d="M0 4h12M9 1l3 3-3 3" fill="none" stroke="currentColor" stroke-width="1"/></svg></span>

<!-- Banner -->
<section class="banner">
  <svg class="abs" style="left:0;top:0;width:1200px;height:312px" viewBox="0 0 1200 312" role="img" aria-label="House roof covered in solar panels under a blue sky">
    <defs><linearGradient id="roofSky" x1="0" y1="0" x2="0" y2="1"><stop offset="0" stop-color="#8fc3ec"/><stop offset=".45" stop-color="#3d5d86"/><stop offset=".75" stop-color="#b0593f"/><stop offset="1" stop-color="#5f8a3c"/></linearGradient></defs>
    <polygon points="718,0 1200,0 1200,312 670,312" fill="url(#roofSky)"/>
  </svg>
  <h2>We use only the best ionic and<br>LoftSuk cleaning systems</h2>
  <span class="btn light" style="left:107px;top:224px;width:137px">Request a Quote
    <svg viewBox="0 0 14 8"><path d="M0 4h12M9 1l3 3-3 3" fill="none" stroke="currentColor" stroke-width="1"/></svg></span>
</section>

<!-- Footer -->
<footer class="footer">
  <span class="f-mark"></span>
  <div class="f-brand">BrightPane</div>

  <div class="f-head" style="left:468px">Contact us <span style="width:120px"></span></div>
  <ul class="f-list" style="left:468px;top:101px">
    <li><svg viewBox="0 0 10 10"><path d="M5 9.5S1.5 6 1.5 4a3.5 3.5 0 017 0c0 2-3.5 5.5-3.5 5.5z" fill="#1fade4"/></svg><span><b>Head Office -</b> Ferndale Rise NSW 2590</span></li>
    <li><svg viewBox="0 0 10 10"><rect x="1" y="2" width="8" height="6" fill="none" stroke="#1fade4"/><path d="M1 2l4 3 4-3" fill="none" stroke="#1fade4"/></svg><span>sales@brightpane.com.au</span></li>
    <li><svg viewBox="0 0 10 10"><path d="M2 1l2 2-1 1.5c.8 1.5 1.5 2.2 3 3L7.5 6l2 2-1.5 1.5C4 9 1 6 .5 2z" fill="#1fade4"/></svg><span><b>Sydney -</b> 02 7391 5083</span></li>
    <li><svg viewBox="0 0 10 10"><path d="M2 1l2 2-1 1.5c.8 1.5 1.5 2.2 3 3L7.5 6l2 2-1.5 1.5C4 9 1 6 .5 2z" fill="#1fade4"/></svg><span><b>Southern Highlands -</b> 02 4860 3178</span></li>
    <li><svg viewBox="0 0 10 10"><path d="M2 1l2 2-1 1.5c.8 1.5 1.5 2.2 3 3L7.5 6l2 2-1.5 1.5C4 9 1 6 .5 2z" fill="#1fade4"/></svg><span><b>Goulburn -</b> 02 4860 3178</span></li>
    <li><svg viewBox="0 0 10 10"><path d="M2 1l2 2-1 1.5c.8 1.5 1.5 2.2 3 3L7.5 6l2 2-1.5 1.5C4 9 1 6 .5 2z" fill="#1fade4"/></svg><span><b>Canberra -</b> 02 6172 8354</span></li>
    <li><svg viewBox="0 0 10 10"><path d="M2 1l2 2-1 1.5c.8 1.5 1.5 2.2 3 3L7.5 6l2 2-1.5 1.5C4 9 1 6 .5 2z" fill="#1fade4"/></svg><span><b>Wollongong -</b> 02 4239 6017</span></li>
  </ul>

  <div class="f-head" style="left:731px">Quick links <span style="width:100px"></span></div>
  <ul class="f-list" style="left:731px;top:106px">
    <li>Home</li><li>Solar Cleaning</li><li>Gutter Cleaning</li><li>Dustora</li><li>Contact us</li><li>Terms and conditions</li><li>Privacy policy</li>
  </ul>

  <span class="social" style="top:100px"></span>
  <span class="social" style="top:137px"></span>
  <span class="social" style="top:174px"></span>
  <span class="social" style="top:212px"></span>

  <div class="legal" style="left:200px">© 2025 <b>BrightPane.</b> All Right Reserved</div>
  <div class="legal" style="left:468px"><b>ABN:</b> 48906237115</div>
  <svg class="abs" style="left:1086px;top:312px;width:12px;height:14px" viewBox="0 0 12 14"><path d="M6 0l6 14-6-4-6 4z" fill="#1fade4"/></svg>
</footer>

</body>
</html>
```